Quiet Horizon Splash page

We want a page to educate the facility managers of Office buildings on the wasted lighting that is left on at night time in their buildings. The page should encourage them to reach out to us for ways to reduce/eliminate the wasted lighting.
Part of the motivation is created by showing photographs of city skylines, and highlight specific buildings, and floors in buildings that have lights left on when the light is not needed. We have attached photos of the San Francisco and LA skylines. We have also created a page with youtube videos educating on light pollution. http://www.velotransit-example.com/education-center-2/velotransit-video-library/
Details:
- We would like a graphic on the page that is the symbol to represent the Quiet Horizon we are working to create.
- The page should be able to segment different cities
- The page should be stand alone with enough information to be valuable, but also should link into more details
- The page should tie into our existing site www.velotransit-example.com
- The page should motivate people to eliminate their wasted light by contacting us
Updates

Hi all, We have received a number of designs, and some are close to our expectation. We will choose a 1st and 2nd place tomorrow night. Here is more clarification based on the designs being submitted: (Please edit your submission if it does not match with the notes below) 1. This design is Not for a homepage or to represent VeloTransit corporately. This design is only to do an interior page that will be the Quiet Horizon initiative. 2. The "Symbol to represent the Quiet Horizon" is a graphic, logo or image that can universally be recognized as representing our Quiet Horizon initiative. This would be used on the webpage and literature we may develop in the future. 3. We expect people visiting this Quiet Horizon page to ask a couple questions. * "What is the Quiet Horizon?" * Is my building causing the wasted lighting (Can I look at a photo of my city {San Francisco, Los Angeles, New York City} and see my building lit up at night? * Is VeloTransit creating a Quiet Horizon? (See images from every 6 months of the same city skyline to see how it is changing) 4. The webpage should not focus on the specific capabilities, skills, tools or software of VeloTransit. It should only focus on the Who, What, Where, Why, How of creating a Quiet Horizon.

Here are notes to help with the design: - Use our uploaded skyline images. - Highlight a level of light left on in those images. and note, "Is your lighting wasted for hours every night?" - Highlight a dark area of a building in those images and note "We helped create a Quiet Horizon here!" - Add an email address to contact us at the bottom and say, "I want to be part of the Quiet Horizon in my city!""

Hi All Designers, Sorry for the delay while I was traveling the past week. We had 62 designs submitted and we have narrowed it down to 7. We are voting this week on designs that are best and then we will choose First place and Second place awards. Thanks! Peter

Target Market(s)

Owners and managers of large office buildings in Western speaking countries. Generally adult male aged 30-60.

Industry/Entity Type

Education

Requirements
Must have
• Sectioned areas for different cities based on where the person is visiting our website from. Major cities we focus on include: Los Angeles, San Francisco, New York City, Philadelphia
Nice to have
• Graphic or image logo representing the Quiet Horizon.
Should not have
• Do not focus on VeloTransit. Focus on the Quiet Horizon initiative.

```html
<!DOCTYPE html>
<html lang="en">
<head>
<meta charset="utf-8">
<title>Quiet Horizon – VeloTransit</title>
<link href="https://fonts.googleapis.com/css2?family=Arimo:wght@400;700&display=swap" rel="stylesheet">
<style>
  :root{
    --white:#ffffff;
    --nav-bg:#f1f1f1;
    --nav-text:#555555;
    --nav-rule:#9a9a9a;
    --night:#27316f;
    --night-deep:#161c4a;
    --night-glow:#3b4a9c;
    --green:#8dc63f;
    --green-light:#a6d35a;
    --ink:#3a3a3a;
    --badge-red:#d9474c;
    --social-blue:#79a6da;
    --amber:#d98a2c;
  }
  *{box-sizing:border-box;margin:0;padding:0}
  html,body{width:900px;height:1200px;overflow:hidden}
  body{
    position:relative;
    background:repeating-linear-gradient(135deg,#f7f7f7 0 6px,#efefef 6px 7px);
    font-family:"Arimo",Arial,sans-serif;
    color:var(--ink);
  }
  .screen{position:absolute;left:103px;width:692px;background:var(--white)}
  .screen--intro{top:0;height:572px}
  .screen--gallery{top:590px;height:576px}

  .site-header{position:relative;height:50px}
  .brand{position:absolute;left:47px;top:4px;font-size:26px;line-height:28px;color:var(--ink);font-weight:400}
  .header-links{position:absolute;right:16px;top:2px;display:flex;gap:10px}
  .header-links span{width:31px;height:31px;border-radius:50%;background:var(--social-blue);box-shadow:0 1px 3px rgba(0,0,0,.35)}
  .header-links .work-badge{background:var(--badge-red)}

  .main-nav{height:34px;background:var(--nav-bg);display:flex;align-items:center;padding-left:9px;border-top:1px solid #e6e6e6}
  .main-nav a{font-size:10px;letter-spacing:.15px;color:var(--nav-text);text-decoration:none;padding:0 13px;border-right:1px solid var(--nav-rule);line-height:18px}
  .main-nav a:last-child{border-right:0}
  .main-nav small{font-size:7px;margin-left:3px}

  .hero{position:absolute;top:84px;left:0;width:692px;height:488px;overflow:hidden}
  .night-sky{position:absolute;inset:0;background:
      radial-gradient(ellipse 60% 25% at 35% 78%,rgba(150,160,210,.45),transparent 70%),
      radial-gradient(ellipse at 50% 85%,var(--night-glow),transparent 60%),
      linear-gradient(180deg,var(--night-deep),var(--night) 60%,#1f2762)}
  .city-silhouette{position:absolute;left:0;right:0;bottom:0;height:120px;background:linear-gradient(180deg,rgba(30,38,90,0),rgba(18,24,64,.9))}
  .tower-photo{position:absolute;right:0;top:0;width:165px;height:340px;background:
      radial-gradient(ellipse 50% 30% at 40% 25%,rgba(200,150,70,.35),transparent 70%),
      radial-gradient(ellipse 50% 30% at 55% 60%,rgba(190,140,60,.25),transparent 70%),
      linear-gradient(180deg,#1c2038,#262a44 65%,rgba(38,48,100,0))}

  .ribbon{position:absolute;background:var(--green);color:#fff;text-align:center}
  .ribbon--top{left:162px;top:0;width:360px;height:44px;clip-path:polygon(0 0,100% 0,94% 100%,6% 100%);font-size:20px;line-height:44px}
  .ribbon--cta{left:257px;top:461px;width:172px;height:27px;clip-path:polygon(6% 0,94% 0,100% 100%,0 100%);font-size:16px;line-height:28px}

  .snapshot{position:absolute;background:#fff;padding:7px;box-shadow:0 2px 6px rgba(0,0,0,.4)}
  .snapshot div{width:100%;height:100%}
  .shot-1{background:radial-gradient(ellipse 40% 30% at 65% 45%,rgba(200,150,60,.5),transparent 70%),linear-gradient(180deg,#0c0e1c,#201a18 60%,#6a4a22)}
  .shot-2{background:radial-gradient(ellipse 45% 45% at 45% 55%,rgba(230,150,50,.8),transparent 70%),linear-gradient(180deg,#1a2a6a,#2a2a55 40%,#8a4a1a 85%,#c0702a)}
  .shot-3{background:radial-gradient(ellipse 50% 35% at 45% 75%,rgba(240,150,40,.85),transparent 70%),linear-gradient(180deg,#0a0c18,#24202a 50%,#b06422)}
  .shot-4{background:radial-gradient(ellipse 40% 40% at 55% 55%,rgba(200,140,60,.55),transparent 70%),linear-gradient(180deg,#0c0e1a,#2a2620 60%,#5a4428)}

  .initiative{position:absolute;left:318px;top:66px;width:200px;color:#fff}
  .idea-icon{position:absolute;left:90px;top:2px}
  .initiative h2{font-size:12px;font-weight:700;text-align:center;margin-top:50px}
  .initiative p{font-size:9.4px;line-height:12.7px;margin:19px 0 0 14px;width:172px}
  .initiative .lead{font-size:12px;font-weight:700;line-height:15.5px;margin:16px 0 0 14px;width:180px}
  .initiative .lead em{font-style:normal;color:var(--green)}

  .campaign-title{position:absolute;left:0;width:692px;top:388px;text-align:center;color:#fff;padding-left:6px}
  .campaign-title h1{font-size:31px;font-weight:700;letter-spacing:.5px;line-height:36px}
  .campaign-title p{font-size:15.5px;margin-top:0}
  .campaign-title p em{font-style:normal;color:var(--green)}

  .city-check{position:absolute;left:529px;top:360px;width:163px;color:#fff}
  .city-check h3{font-size:9.5px;font-weight:700;text-align:right;padding-right:14px}
  .city-check .check-bar{margin-top:9px;background:var(--green);font-size:9.5px;font-weight:700;height:20px;line-height:20px;padding-left:13px;clip-path:polygon(4% 0,100% 0,100% 100%,0 100%)}
  .city-check ul{list-style:none;margin-top:2px}
  .city-check li{display:flex;justify-content:space-between;align-items:center;padding:0 25px 0 49px;height:23px}
  .city-check li::before{content:"";border-left:7px solid var(--green);border-top:4.5px solid transparent;border-bottom:4.5px solid transparent}
  .city-check a{color:var(--green-light);font-size:9.5px;font-weight:700;text-decoration:underline}

  .gallery{position:absolute;top:83px;left:0;width:692px;height:490px;overflow:hidden}
  .gallery .night-sky{background:
      radial-gradient(ellipse 45% 20% at 30% 82%,rgba(140,150,210,.35),transparent 70%),
      radial-gradient(ellipse at 50% 90%,var(--night-glow),transparent 55%),
      linear-gradient(180deg,#20295f,var(--night) 50%,#1d2560)}
  .city-frame{position:absolute;left:70px;top:54px;width:551px;height:314px;border:1px solid var(--green);box-shadow:0 6px 10px rgba(0,0,0,.5);background:
      radial-gradient(ellipse 12% 30% at 30% 45%,rgba(141,198,63,.35),transparent 70%),
      radial-gradient(ellipse 12% 35% at 62% 40%,rgba(141,198,63,.35),transparent 70%),
      radial-gradient(ellipse 10% 20% at 44% 55%,rgba(141,198,63,.3),transparent 70%),
      radial-gradient(ellipse 60% 25% at 50% 88%,#6a6a6a,transparent 75%),
      linear-gradient(180deg,#050505,#1a1a1a 60%,#3a3a3a)}
  .slide-arrow{position:absolute;top:192px}
  .slide-arrow--prev{left:36px}
  .slide-arrow--next{left:636px}
  .city-caption{position:absolute;top:413px;width:692px;text-align:center;color:#fff;font-size:16px;padding-right:12px}
  .gallery-edge{position:absolute;left:155px;top:573px;width:410px;height:3px;background:var(--green)}
</style>
</head>
<body>

<section class="screen screen--intro">
  <header class="site-header">
    <div class="brand">VeloTransit</div>
    <div class="header-links">
      <span class="work-badge"></span><span></span><span></span><span></span>
    </div>
  </header>
  <nav class="main-nav">
    <a>Home</a><a>Commercial<small>▸</small></a><a>Residential<small>▸</small></a><a>Field Services Division</a><a>Education Center<small>▸</small></a><a>Our Company<small>▸</small></a>
  </nav>

  <div class="hero">
    <div class="night-sky" role="img" aria-label="City skyline at night under a deep blue sky with clouds and a moon"></div>
    <div class="tower-photo" role="img" aria-label="Office tower at night with many lit windows"></div>
    <div class="city-silhouette"></div>

    <div class="ribbon ribbon--top">Save energy and enviroment</div>

    <div class="snapshot" style="left:22px;top:86px;width:132px;height:118px"><div class="shot-1" role="img" aria-label="Downtown towers lit at night"></div></div>
    <div class="snapshot" style="left:172px;top:84px;width:130px;height:122px"><div class="shot-2" role="img" aria-label="Waterfront skyline with lit office buildings"></div></div>
    <div class="snapshot" style="left:20px;top:221px;width:133px;height:123px"><div class="shot-3" role="img" aria-label="City buildings glowing orange at night"></div></div>
    <div class="snapshot" style="left:174px;top:221px;width:128px;height:124px"><div class="shot-4" role="img" aria-label="Night skyline seen from above"></div></div>

    <div class="initiative">
      <svg class="idea-icon" width="20" height="32" viewBox="0 0 20 32" fill="none" stroke="#fff" stroke-width="1.2">
        <path d="M10 1a8 8 0 0 0-5 14c1.5 1.3 2 3 2 5h6c0-2 .5-3.7 2-5A8 8 0 0 0 10 1z"/>
        <path d="M7 23h6M7 26h6M8.5 29h3"/>
      </svg>
      <h2>What is Quiet Horizon Initiative?</h2>
      <p>Wasted lighting that is left on at night time in office buildings not only produces unnecessary costs but also harms the enviroment. Light polution can be hazardous to the health of both humans and wildlife.</p>
      <p class="lead">The Quiet Horizon Initiative is here to help you <em>reduce or eliminate wasted lighting</em> in your buildings.</p>
    </div>

    <div class="campaign-title">
      <h1>QUIET HORIZON</h1>
      <p>Let your office sleep. <em>Save energy.</em></p>
    </div>

    <div class="city-check">
      <h3>Are all those ligts needed?</h3>
      <div class="check-bar">Check your buildings now:</div>
      <ul>
        <li><a>San Francisco</a></li>
        <li><a>New York City</a></li>
        <li><a>Los Angeles</a></li>
      </ul>
    </div>

    <div class="ribbon ribbon--cta">Learn More</div>
  </div>
</section>

<section class="screen screen--gallery">
  <header class="site-header">
    <div class="brand">VeloTransit</div>
    <div class="header-links">
      <span class="work-badge"></span><span></span><span></span><span></span>
    </div>
  </header>
  <nav class="main-nav">
    <a>Home</a><a>Commercial<small>▸</small></a><a>Residential<small>▸</small></a><a>Field Services Division</a><a>Education Center<small>▸</small></a><a>Our Company<small>▸</small></a>
  </nav>

  <div class="gallery">
    <div class="night-sky" role="img" aria-label="Blurred night skyline backdrop in deep blue"></div>
    <div class="city-silhouette"></div>
    <div class="city-frame" role="img" aria-label="Black and white night photo of city towers with lit windows highlighted in green"></div>
    <svg class="slide-arrow slide-arrow--prev" width="16" height="28" viewBox="0 0 16 28"><path d="M16 0v28L0 14z" fill="var(--green)"/></svg>
    <svg class="slide-arrow slide-arrow--next" width="16" height="28" viewBox="0 0 16 28"><path d="M0 0v28l16-14z" fill="var(--green)"/></svg>
    <div class="city-caption">New York City</div>
  </div>
  <div class="gallery-edge"></div>
</section>

</body>
</html>
```